Velt Risk Management - Harbor Pathway

Upgrade existing PP per the upload. I will use this to email to Prospects and clients as well as posting to our website.
Edit and update pages - this PP was created several years ago and needs a full update based on the same content. Better graphics etc etc are needed
Create some links to websites
Velt Risk Management is a professional consultant where owners have MBA's. Law Degrees and CPCU Designation. PP should be designed with this in mind similar to resources used by CPA's, Accountants or Financial Advisors
Updates
Need extra days to review
Target Market(s)
Construction Contractors
Colors
Designer to choose colors to be used in the design.
Requirements
Must have
- Follow existing PP
Nice to have
- Take a look at our current website which will be upgraded when PP is complete
- www.tarvelpointe.biz

```html
<!DOCTYPE html>
<html lang="en">
<head>
<meta charset="utf-8">
<title>Buildwise Counsel – Presentation Overview</title>
<link href="https://fonts.googleapis.com/css2?family=Carlito:wght@400;700&family=Roboto+Slab:wght@700;900&display=swap" rel="stylesheet">
<style>
  :root {
    --page: #ffffff;
    --ink: #1a1a1a;
    --body: #262626;
    --accent: #e2d81f;
    --charcoal: #3a3a3a;
    --photo-dark: #4a4744;
    --photo-mid: #8a8580;
    --photo-warm: #a48a6a;
    --link: #3b5fc0;
  }
  * { box-sizing: border-box; margin: 0; padding: 0; }
  html, body { width: 1029px; height: 1200px; overflow: hidden; background: var(--page); }
  body { position: relative; font-family: "Carlito", "Calibri", sans-serif; color: var(--body); }

  .slide { position: absolute; width: 414px; height: 308px; overflow: hidden; background: var(--page); }
  .abs { position: absolute; }

  .heading {
    position: absolute; display: flex; align-items: center; gap: 12px;
    font-family: "Roboto Slab", serif; font-weight: 900; font-size: 16px; color: var(--ink);
  }
  .heading-mark { width: 20px; height: 16px; background: var(--accent); border-left: 4px solid var(--ink); }

  .bullets { position: absolute; list-style: none; font-size: 11px; line-height: 13px; }
  .bullets li { position: relative; padding-left: 14px; }
  .bullets li::before {
    content: ""; position: absolute; left: 0; top: 2px; width: 8px; height: 8px;
    border: 1px solid var(--accent);
  }

  .photo-crane { background: linear-gradient(180deg, var(--photo-mid) 0%, var(--photo-dark) 100%); }
  .photo-crane-wide { background: linear-gradient(90deg, var(--photo-dark) 0%, var(--photo-mid) 50%, var(--photo-dark) 100%); }
  .band-accent { background: var(--accent); }

  /* Title slide */
  .cover { left: 41px; top: 134px; }
  .cover-photo { inset: 0; background: linear-gradient(120deg, #c9c2b8 0%, #8d7f6e 45%, var(--photo-warm) 70%, #5c4e40 100%); }
  .cover-title {
    left: 38px; top: 50px; font-family: "Roboto Slab", serif; font-weight: 900;
    font-size: 24px; color: var(--ink); letter-spacing: -0.3px;
  }
  .cover-sub { left: 20px; top: 80px; font-size: 9px; font-weight: 700; color: var(--ink); }
  .cover-link { left: 280px; top: 286px; font-size: 9px; color: var(--link); text-decoration: underline; }

  /* Mission */
  .mission { left: 528px; top: 134px; }

  /* Philosophy */
  .philosophy { left: 41px; top: 473px; }
  .philosophy-text { left: 40px; top: 66px; width: 240px; font-size: 11px; line-height: 13px; }

  /* Goals */
  .goals { left: 528px; top: 473px; }

  /* Assumptions */
  .assumptions { left: 44px; top: 823px; height: 290px; }
  .assumption-list { position: absolute; left: 47px; list-style: none; font-size: 11px; line-height: 13px; }
  .assumption-list li { position: absolute; left: 0; width: 330px; padding-left: 23px; white-space: normal; }
  .assumption-letter { position: absolute; left: 0; top: -3px; color: var(--accent); font-size: 14px; }

  /* Leadership */
  .leadership { left: 528px; top: 823px; height: 290px; }
  .quote-author { left: 67px; top: 110px; font-family: "Roboto Slab", serif; font-weight: 700; font-size: 10px; color: var(--ink); }
  .quote-box { left: 63px; top: 126px; width: 296px; height: 106px; display: flex; }
  .quote { flex: 1; display: flex; align-items: center; justify-content: center; text-align: center;
           font-size: 10.5px; font-weight: 700; line-height: 12px; padding: 0 12px; }
  .quote-leader { background: var(--charcoal); color: var(--accent); flex: 0 0 140px; }
  .quote-manager { background: var(--accent); color: var(--ink); }
</style>
</head>
<body>

  <section class="slide cover">
    <div class="abs cover-photo" role="img" aria-label="Photo of a contractor in a hard hat reviewing plans at a desk with a laptop and tools"></div>
    <h1 class="abs cover-title">Buildwise Counsel</h1>
    <p class="abs cover-sub">Management Consultants for the Construction Industry</p>
    <a class="abs cover-link" href="https://www.tarvelpointe.biz">www.tarvelpointe.biz</a>
  </section>

  <section class="slide mission">
    <div class="abs band-accent" style="left:0;top:0;width:23px;height:308px"></div>
    <div class="abs photo-crane" style="left:23px;top:0;width:101px;height:308px" role="img" aria-label="Monochrome photo of tower cranes over a building site"></div>
    <h2 class="heading" style="left:134px;top:18px">
      <span class="heading-mark"></span>Mission Statement
    </h2>
    <ul class="bullets" style="left:136px;top:74px;width:270px">
      <li>To provide the highest level of personal financial services in a friendly, professional manner</li>
      <li style="margin-top:22px">To encourage contractor clients to establish and extend effective management systems in their companies</li>
      <li style="margin-top:22px">To increase the knowledge and ability of our clients to manage and control their financial well-being</li>
      <li style="margin-top:22px">To provide sound financial/operating management advice in order to maximize clients corporate value while minimizing risk</li>
    </ul>
  </section>

  <section class="slide philosophy">
    <h2 class="heading" style="left:21px;top:71px;top:17px">
      <span class="heading-mark"></span>Buildwise Counsel Philosophy
    </h2>
    <div class="abs photo-crane" style="left:294px;top:0;width:100px;height:308px" role="img" aria-label="Monochrome photo of cranes above concrete columns"></div>
    <div class="abs band-accent" style="left:394px;top:0;width:20px;height:308px"></div>
    <ul class="bullets" style="left:40px;top:66px;width:240px">
      <li>Buildwise Counsel is dedicated to the safe and successful growth of their construction clients by strategically implementing comprehensive and practical management systems. BWC will minimize business risk by maximizing critical information flows to the CEO. Throughout the organization, BWC will provide the Client CEO with the necessary tools for the critical information needed to manage his growing company. The objective is to maximize company value and minimize business risk</li>
    </ul>
  </section>

  <section class="slide goals">
    <h2 class="heading" style="left:21px;top:19px">
      <span class="heading-mark"></span>Goals and Objectives
    </h2>
    <ul class="bullets" style="left:34px;top:59px;width:360px">
      <li>Review Why Contractors Fail</li>
      <li style="margin-top:5px">Focus on Why Contractors Succeed</li>
      <li style="margin-top:5px">Establish Basic Premise - Knowledge/Education/Commitment to Change will bridge the gap for success</li>
      <li style="margin-top:22px">Implement Contractors Navigation System to accomplish Mission Statement</li>
      <li style="margin-top:22px">Support Client in the continuing commitment to use the Integrated Management Systems put in place</li>
    </ul>
    <div class="abs photo-crane-wide" style="left:0;top:236px;width:414px;height:56px" role="img" aria-label="Monochrome panorama of tower cranes against the sky"></div>
    <div class="abs band-accent" style="left:0;top:292px;width:414px;height:16px"></div>
  </section>

  <section class="slide assumptions">
    <div class="abs band-accent" style="left:0;top:0;width:414px;height:17px"></div>
    <div class="abs photo-crane-wide" style="left:0;top:17px;width:414px;height:51px" role="img" aria-label="Monochrome panorama of tower cranes against the sky"></div>
    <h2 class="heading" style="left:21px;top:78px">
      <span class="heading-mark"></span>Basic Assumptions
    </h2>
    <ol class="assumption-list" style="top:0">
      <li style="top:117px"><span class="assumption-letter">A.</span>Construction Companies need to be Micro Managed</li>
      <li style="top:147px"><span class="assumption-letter">B.</span>Construction Companies Require a High Level of Standardization in a Non Standardized Industry</li>
      <li style="top:190px"><span class="assumption-letter">C.</span>Manage the Negative Variances</li>
      <li style="top:221px"><span class="assumption-letter">D.</span>Construction Companies fall into Project Based or Management Based Models</li>
      <li style="top:264px"><span class="assumption-letter">E.</span>Growing Construction Companies require the proper balance between Leadership and Management</li>
    </ol>
  </section>

  <section class="slide leadership">
    <h2 class="heading" style="left:24px;top:18px">
      <span class="heading-mark"></span>Leadership / Management
    </h2>
    <p class="abs quote-author">Marlon Hastings</p>
    <div class="abs quote-box">
      <p class="quote quote-leader">“Leaders are people who do the right thing”</p>
      <p class="quote quote-manager">“Managers are people who do things right”</p>
    </div>
  </section>

</body>
</html>
```